QRL Infographic Design and Business Card design

We have an infographic but it could use some updating and creativity applied to it. Would like to match it a bit more to our current logo and web design (although it doesn’t have to match per se, thinking of updating it too) http://qrl-advisory.example/QRL_Advisory/QRL_Advisory___Your_treasury_pricing_and_fee_negotiation_specialists.html
Can be double sided

Target Market(s)

Companies that make more than $150MM a year

Industry/Entity Type

Business

Contact Information for Business Card

Uploaded the logo and you can also look at the website.

Font styles to use
Sans Serif

Requirements
Must have
• Must look professional. Looking to stick to the same colors in the logo, the logo won’t change. Very open after that
Nice to have
• Front and back on the card

```html
<!DOCTYPE html>
<html lang="en">
<head>
<meta charset="utf-8">
<title>QRL Advisory – Business Card</title>
<link href="https://fonts.googleapis.com/css2?family=Arimo:wght@400;700&display=swap" rel="stylesheet">
<style>
  :root {
    --backdrop: #e9e6e1;
    --card-red: #b3261b;
    --card-red-dark: #8f1b12;
    --card-white: #ffffff;
    --accent-red: #b8241a;
    --text-grey: #6f6f6f;
    --rule-grey: #9a9a9a;
    --white: #ffffff;
  }
  * { box-sizing: border-box; margin: 0; padding: 0; }
  html, body {
    width: 1200px; height: 950px; overflow: hidden;
    background: var(--backdrop);
    font-family: "Arimo", Arial, sans-serif;
  }
  .sheet {
    width: 1200px; height: 950px;
    display: flex; flex-direction: column; align-items: center; justify-content: center;
    gap: 50px;
  }
  .card {
    width: 700px; height: 400px; position: relative;
    box-shadow: 0 6px 18px rgba(0,0,0,.22);
  }

  /* Front */
  .card-front {
    background: linear-gradient(135deg, var(--card-red) 0%, #c23a2e 55%, var(--card-red-dark) 100%);
    display: flex; flex-direction: column; align-items: center; justify-content: center;
    color: var(--white);
  }
  .front-name { font-size: 50px; font-weight: 700; color: var(--white); line-height: 1; }
  .front-web { margin-top: 14px; font-size: 24px; font-weight: 700; color: var(--white); }

  /* Back */
  .card-back { background: var(--card-white); }
  .back-brand {
    position: absolute; right: 60px; top: 52px;
    text-align: right;
  }
  .back-name { font-size: 42px; font-weight: 700; color: var(--accent-red); line-height: 1; }
  .back-web { font-size: 20px; font-weight: 700; color: var(--text-grey); margin-top: 10px; }
  .top-rule {
    position: absolute; top: 160px; right: 60px; width: 280px;
    border-top: 1.5px solid var(--rule-grey);
  }
  .address {
    position: absolute; right: 60px; top: 180px;
    text-align: right; font-style: normal;
    font-size: 17px; line-height: 1.4; color: var(--text-grey);
  }
  .contact { position: absolute; left: 50px; bottom: 40px; color: var(--text-grey); }
  .person-row { display: flex; align-items: flex-end; gap: 8px; }
  .person-name { font-size: 24px; font-weight: 700; color: var(--accent-red); line-height: 1.1; }
  .person-rule { width: 180px; border-top: 1.5px solid var(--rule-grey); margin-bottom: 5px; }
  .person-title { font-size: 17px; margin: 4px 0 10px 14px; }
  .contact-list { list-style: none; font-size: 17px; line-height: 1.5; }
  .contact-list .label { color: var(--accent-red); font-weight: 700; display: inline-block; width: 18px; }
</style>
</head>
<body>
<main class="sheet">
  <section class="card card-front" aria-label="Card front">
    <p class="front-name">QRL</p>
    <p class="front-web">QRL-Advisory.example</p>
  </section>

  <section class="card card-back" aria-label="Card back">
    <div class="back-brand">
      <p class="back-name">QRL</p>
      <p class="back-web">QRL-Advisory.example</p>
    </div>
    <div class="top-rule"></div>
    <address class="address">
      4120 Birchwood Court<br>Fairbanks<br>Alaska 99701
    </address>

    <div class="contact">
      <div class="person-row">
        <h1 class="person-name">Daniel Marsh</h1>
        <span class="person-rule"></span>
      </div>
      <p class="person-title">CEO/Founder</p>
      <ul class="contact-list">
        <li><span class="label">P</span>: 555 214 7730</li>
        <li><span class="label">C</span>: 555 382 6190</li>
        <li><span class="label">F</span>: 555 907 4418</li>
        <li><span class="label">E</span>: daniel@qrl-advisory.example</li>
      </ul>
    </div>
  </section>
</main>
</body>
</html>
```